Italian restaurant needs new site

Need to make our website better.

Must have reservation module

Must be able to sell wine tasting tours and wine pairing tours and intégrate with tolvo desk

Blog

Social media

Wandermeter ranking and last review.

Number of Pages Required

1 page

Font styles to use
Serif

Requirements
Must have
• Reservation module
• Marketplace to buy wine pairings and gift certificates
• Wandermeter review
• Chatterly posts
• All info from old site

```html
<!DOCTYPE html>
<html lang="en">
<head>
<meta charset="utf-8">
<title>Vinora Bistro – Italian Restaurant in Cabo San Lucas</title>
<link href="https://fonts.googleapis.com/css2?family=Great+Vibes&family=Roboto+Slab:wght@300;400;700&family=Open+Sans:wght@400;600&display=swap" rel="stylesheet">
<style>
:root{
  --wine:#9a1c22;
  --ink:#2a2522;
  --dark:#1e1916;
  --wood:#3a2a22;
  --gold:#d8b26a;
  --paper:#ffffff;
  --mist:#f1f0ee;
  --line:#d9d6d2;
  --muted:#7b746f;
  --light-text:#e9e4de;
  --chat-bar:#3d5a96;
}
*{box-sizing:border-box;margin:0;padding:0}
html,body{width:1200px;height:4100px;overflow:hidden}
body{font-family:"Open Sans",Arial,sans-serif;color:var(--ink);background:var(--paper);font-size:13px;line-height:1.6}
section,footer{position:relative;width:1200px;overflow:hidden}
.photo{position:absolute}
.eyebrow{font-family:"Great Vibes",cursive;font-size:30px;line-height:1;display:block}
.heading{font-family:"Roboto Slab",Georgia,serif;font-weight:400;font-size:40px;line-height:1.1}
.btn{display:inline-block;font-family:"Roboto Slab",Georgia,serif;font-size:13px;padding:10px 20px;text-decoration:none}
.btn-wine{background:var(--wine);color:#fff}
.btn-ghost{color:var(--wine);border-left:3px solid var(--wine);padding:8px 14px;background:transparent}
.btn-light{color:#fff}
.btn-dark{background:rgba(0,0,0,.55);color:#fff;border-left:3px solid var(--wine)}

/* Hero */
.hero{height:560px;background:var(--dark)}
.hero .photo{inset:0;background:radial-gradient(ellipse at 60% 45%,#8a6a4c 0%,#4a3628 40%,#1d1612 85%)}
.logo{position:absolute;left:40px;top:0;width:150px;height:118px;background:#fff;display:flex;flex-direction:column;align-items:center;justify-content:center;box-shadow:0 2px 8px rgba(0,0,0,.3)}
.logo span{font-family:"Roboto Slab",Georgia,serif;color:var(--wine);font-size:28px;font-weight:700;line-height:1.1}
.nav{position:absolute;right:40px;top:22px;display:flex;gap:4px}
.nav a{color:#fff;text-decoration:none;font-family:"Roboto Slab",Georgia,serif;font-size:14px;padding:8px 14px}
.nav a.active{background:var(--wine)}
.hero-title{position:absolute;left:0;right:0;top:225px;text-align:center;color:#fff}
.hero-title .eyebrow{color:var(--gold);font-size:44px}
.hero-title h1{font-family:"Roboto Slab",Georgia,serif;font-weight:300;font-size:44px;line-height:1.2;text-shadow:0 2px 6px rgba(0,0,0,.5)}
.down-tab{position:absolute;bottom:0;left:560px;width:80px;height:26px}

/* Welcome */
.welcome{height:480px;background:var(--paper)}
.welcome .photo{left:100px;top:120px;width:440px;height:230px;background:linear-gradient(135deg,#f3f1ee,#c9c2b8 55%,#5a1418)}
.welcome .text{position:absolute;left:640px;top:125px;width:440px}
.welcome p,.dishes p{color:var(--muted);font-size:13px;margin:12px 0 20px}
.welcome .eyebrow,.dishes .eyebrow{color:var(--wine)}

/* Reservations */
.reservations{height:340px;background:var(--wood)}
.reservations .photo{inset:0;background:linear-gradient(90deg,#1b1512 0%,#2d221c 35%,#6a5a4c 70%,#3b2f27 100%)}
.reservations .text{position:absolute;left:150px;top:55px;width:330px;color:var(--light-text)}
.reservations .eyebrow,.reservations .heading{color:#fff}
.reservations p{color:#cfc6bd;margin:12px 0 22px;font-size:12px}

/* Dishes */
.dishes{height:480px;background:var(--paper)}
.dishes .photo{left:120px;top:70px;width:270px;height:270px;border-radius:50%;background:radial-gradient(circle,#7d9a3e 0%,#c9c9a8 45%,#f5f5f2 75%)}
.dishes .text{position:absolute;left:640px;top:110px;width:440px}
.dots{position:absolute;left:580px;top:415px;display:flex;gap:6px}
.dots i{width:9px;height:9px;border-radius:50%;background:var(--line)}
.dots i.on{background:var(--muted)}

/* Mission */
.mission{height:320px;background:var(--wood)}
.mission .photo{inset:0;background:linear-gradient(90deg,#2a1c16 0%,#4a3024 55%,#6b3a22 80%,#a8421f 100%)}
.mission .text{position:absolute;left:150px;top:50px;width:520px;color:#fff}
.mission .eyebrow{color:#fff}
.mission p{color:#d9cfc5;font-size:12px;margin-top:12px}

/* Menu */
.menu{height:600px;background:var(--mist)}
.menu .photo.pasta{left:0;top:390px;width:110px;height:200px;background:linear-gradient(160deg,#f2d27a,#d9a84a)}
.menu .photo.bottle{right:0;top:360px;width:140px;height:150px;background:linear-gradient(200deg,#2a2a26,#6c1a1c)}
.menu .photo.tomato{right:90px;top:70px;width:90px;height:90px;border-radius:50%;background:radial-gradient(circle,#e2432a,#9b2210)}
.menu-title{text-align:center;padding-top:45px}
.menu-title .eyebrow{color:var(--ink);font-size:34px}
.menu-title .heading{font-size:44px}
.menu-cols{position:absolute;left:170px;top:175px;width:860px;display:flex;justify-content:space-between}
.menu-col{width:250px}
.menu-col h3{font-family:"Great Vibes",cursive;font-weight:400;font-size:26px;color:var(--ink);border-bottom:1px solid var(--line);padding-bottom:6px;margin-bottom:16px}
.dish{margin-bottom:22px}
.dish b{font-family:"Roboto Slab",Georgia,serif;font-weight:400;font-size:14px;display:block}
.dish span{color:var(--muted);font-size:11px;display:block}
.dish em{font-style:normal;color:var(--wine);font-family:"Roboto Slab",Georgia,serif;font-size:15px}
.menu .btn{position:absolute;left:540px;top:535px}

/* Tours */
.tours{height:300px;background:var(--dark)}
.tours .photo.bg{inset:0;background:linear-gradient(90deg,#2a2019,#1b1511 60%,#2c221b)}
.tours .photo.guest{left:150px;top:50px;width:380px;height:210px;background:linear-gradient(135deg,#8c6e55,#c9a27e 50%,#5a3f2c)}
.tours .text{position:absolute;left:620px;top:50px;width:420px;color:#fff}
.tours .eyebrow{color:#fff}
.tours p{color:#cfc6bd;font-size:12px;margin:12px 0 18px}

/* Blog */
.blog{height:500px;background:linear-gradient(180deg,#f6f6f6,#e7e7e7)}
.blog-head{position:absolute;left:155px;top:40px}
.blog-head .eyebrow{color:var(--ink)}
.cards{position:absolute;left:155px;top:135px;display:flex;gap:20px}
.card{width:283px}
.card .thumb{height:170px;background:linear-gradient(135deg,#7a4a3a,#c89a7e 50%,#4b3a30)}
.card h4{font-family:"Roboto Slab",Georgia,serif;font-weight:400;font-size:15px;margin:14px 0 6px}
.card p{font-size:11px;color:var(--muted)}
.card .meta{display:flex;gap:8px;margin-top:12px}
.card .meta i{width:22px;height:22px;border-radius:50%;background:#555}

/* Footer */
.site-footer{height:460px;background:#15110f;color:var(--light-text)}
.site-footer .photo{inset:0;background:linear-gradient(180deg,#2b221d,#120e0c)}
.fcols{position:absolute;left:155px;top:40px;width:890px;display:flex;gap:22px}
.fcol{width:205px}
.fcol h5{font-family:"Roboto Slab",Georgia,serif;font-weight:400;font-size:15px;color:#fff;margin-bottom:14px}
.fcol h5.gap{margin-top:22px}
.fcol p{font-size:11px;color:#bfb6ad;margin-bottom:10px}
.newsletter{display:flex;margin-top:4px}
.newsletter span{flex:1;height:30px;background:#fff}
.newsletter b{width:34px;height:30px;background:var(--wine)}
.widget{background:#fff;color:var(--ink);height:340px;padding:10px;font-size:10px;overflow:hidden}
.widget .bar{background:var(--chat-bar);color:#fff;font-weight:600;padding:6px 8px;font-size:12px;margin:-10px -10px 8px}
.post{display:flex;gap:8px;margin-bottom:9px;line-height:1.35}
.post i{flex:0 0 34px;height:34px;background:#b9b2aa}
.review .title{font-family:"Roboto Slab",Georgia,serif;font-size:14px;font-weight:700;color:var(--ink);margin-bottom:6px}
.review .score{display:block;font-family:"Roboto Slab",Georgia,serif;font-size:11px;color:var(--wine);margin:3px 0 6px}
.review hr{border:0;border-top:1px solid var(--line);margin:8px 0}
.map{height:340px;background:linear-gradient(135deg,#cfe1ea,#e9e6dc 45%,#bcd3b0)}
.bottom-bar{height:60px;background:#0c0908;color:#8f857c;font-size:11px;text-align:center;line-height:60px}
</style>
</head>
<body>

<section class="hero">
  <div class="photo" role="img" aria-label="Dimly lit restaurant dining table with wine glasses, folded napkins and a bottle of red wine"></div>
  <div class="logo"><span>Vinora</span><span>bistro</span></div>
  <nav class="nav">
    <a class="active" href="#">Home</a><a href="#">About</a><a href="#">Menu</a><a href="#">Reservations</a><a href="#">Tours</a><a href="#">Blog</a><a href="#">Contact</a>
  </nav>
  <div class="hero-title">
    <span class="eyebrow">Vinora Bistro</span>
    <h1>Italian Restaurant In<br>Cabo San Lucas</h1>
  </div>
  <svg class="down-tab" viewBox="0 0 80 26" aria-hidden="true"><path d="M0 26 L40 0 L80 26Z" fill="#fff"/><path d="M33 14 L40 20 L47 14" stroke="#9a1c22" stroke-width="2" fill="none"/></svg>
</section>

<section class="welcome">
  <div class="photo" role="img" aria-label="Bottle of red wine resting in a wrought iron wine holder"></div>
  <div class="text">
    <span class="eyebrow">Welcome to</span>
    <h2 class="heading">Vinora Bistro</h2>
    <p>Vinora Bistro is located in the heart of downtown, across from the marina and plaza. Enjoy fresh pasta, wood fired dishes and fine wine in a warm and friendly room, where every guest is treated like family and every evening feels like a small celebration with friends.</p>
    <a class="btn btn-ghost" href="#">Read More</a>
  </div>
</section>

<section class="reservations">
  <div class="photo" role="img" aria-label="Restaurant table set for dinner beside a window"></div>
  <div class="text">
    <span class="eyebrow">Your</span>
    <h2 class="heading">Reservations</h2>
    <p>Reservations for Vinora Bistro in Cabo San Lucas. Book your table online in a few clicks and we will confirm your evening by email. Groups and private events are welcome too.</p>
    <a class="btn btn-dark" href="#">Book a Table</a>
  </div>
</section>

<section class="dishes">
  <div class="photo" role="img" aria-label="Fresh salad with cheese and olives on a white plate"></div>
  <div class="text">
    <span class="eyebrow">Our</span>
    <h2 class="heading">Favourite Dishes</h2>
    <p>Simple recipes from old family kitchens, made every day with local produce. Our chefs prepare hand rolled pasta, slow cooked sauces and crisp salads dressed with olive oil and herbs. Each plate is paired with a wine from our cellar, chosen to bring out the best of the dish. Come taste the flavours of Italy served with the warm spirit of the coast, and ask our team for the dish of the day.</p>
    <a class="btn btn-ghost" href="#">Read More</a>
  </div>
  <div class="dots"><i class="on"></i><i></i><i></i></div>
</section>

<section class="mission">
  <div class="photo" role="img" aria-label="Dark wooden board with tomatoes, peppers and fresh vegetables"></div>
  <div class="text">
    <span class="eyebrow">Our Mission</span>
    <h2 class="heading">Is Simple</h2>
    <p>To gather friends around good food, honest wine and a table that always has room for one more. We cook with care, we pour with pride and we welcome every guest as family. From the first glass to the last espresso, our aim is a relaxed evening you will want to repeat. That is the promise we keep, night after night, in the heart of Cabo San Lucas.</p>
  </div>
</section>

<section class="menu">
  <div class="photo pasta" role="img" aria-label="Bundle of dry spaghetti"></div>
  <div class="photo tomato" role="img" aria-label="Ripe red tomatoes"></div>
  <div class="photo bottle" role="img" aria-label="Wine bottle lying on its side"></div>
  <div class="menu-title">
    <span class="eyebrow">Our</span>
    <h2 class="heading">Menu</h2>
  </div>
  <div class="menu-cols">
    <div class="menu-col">
      <h3>Entrees</h3>
      <div class="dish"><b>Spanish tortilla</b><span>Potato, onion and fresh herbs</span><em>$ 159</em></div>
      <div class="dish"><b>Spicy Soufflé</b><span>Cheese, chili and garden greens</span><em>$ 159</em></div>
      <div class="dish"><b>Bread Pot</b><span>Warm bread with olive oil dip</span><em>$ 159</em></div>
    </div>
    <div class="menu-col">
      <h3>Antipastos</h3>
      <div class="dish"><b>Bruschetta Classica</b><span>Bread, tomato and basil</span><em>$ 159</em></div>
      <div class="dish"><b>Bruschetta fresco</b><span>Tomato, garlic and mozzarella</span><em>$ 159</em></div>
      <div class="dish"><b>Bruschetta Bianca</b><span>Ricotta, honey and walnut</span><em>$ 159</em></div>
    </div>
    <div class="menu-col">
      <h3>Cocktails</h3>
      <div class="dish"><b>Americano</b><span>Bitter, vermouth and soda</span><em>$ 159</em></div>
      <div class="dish"><b>Negroni</b><span>Gin, bitter and red vermouth</span><em>$ 159</em></div>
      <div class="dish"><b>Negroni Sbagliato</b><span>Bitter, vermouth and prosecco</span><em>$ 159</em></div>
    </div>
  </div>
  <a class="btn btn-wine" href="#">View All Menu</a>
</section>

<section class="tours">
  <div class="photo bg" role="img" aria-label="Dark wine cellar background"></div>
  <div class="photo guest" role="img" aria-label="Guest tasting a glass of red wine"></div>
  <div class="text">
    <span class="eyebrow">Wine</span>
    <h2 class="heading">Tasting Tours</h2>
    <p>Join our sommelier for a guided tasting of regional and Italian wines, paired with small plates from the kitchen. Tours and pairing dinners can be booked online through tolvo desk, and gift certificates are available.</p>
    <a class="btn btn-ghost btn-light" href="#">Book Now</a>
  </div>
</section>

<section class="blog">
  <div class="blog-head">
    <span class="eyebrow">Our</span>
    <h2 class="heading">Blog</h2>
  </div>
  <div class="cards">
    <article class="card">
      <div class="thumb" role="img" aria-label="Friends sharing dinner at the restaurant"></div>
      <h4>A night of pasta and wine</h4>
      <p>Stories from our kitchen, new dishes on the menu and notes from recent dinners with guests.</p>
      <div class="meta"><i></i><i></i></div>
    </article>
    <article class="card">
      <div class="thumb" role="img" aria-label="Chef presenting a dish to guests"></div>
      <h4>Meet the chef behind the menu</h4>
      <p>Our head chef shares the recipes and the markets that shape every plate we serve.</p>
      <div class="meta"><i></i><i></i></div>
    </article>
    <article class="card">
      <div class="thumb" role="img" aria-label="Group of guests raising glasses at a long table"></div>
      <h4>Celebrations at the bistro</h4>
      <p>Birthdays, anniversaries and long tables of friends, all toasted with a glass of good wine.</p>
      <div class="meta"><i></i><i></i></div>
    </article>
  </div>
</section>

<footer class="site-footer">
  <div class="photo" role="img" aria-label="Shelves of wine bottles in a dim cellar"></div>
  <div class="fcols">
    <div class="fcol">
      <h5>Contact Us</h5>
      <p>Calle Marina 12, Centro<br>Cabo San Lucas, B.C.S.<br>+52 000 000 0000<br>hello@vinorabistro.example</p>
      <h5 class="gap">Opening Hours</h5>
      <p>Monday – Sunday<br>5:00 pm – 11:00 pm</p>
      <h5 class="gap">Newsletter</h5>
      <div class="newsletter"><span></span><b></b></div>
    </div>
    <div class="fcol">
      <h5>Follow Us</h5>
      <div class="widget">
        <div class="bar">Chatterly</div>
        <div class="post"><i></i><span>New tasting menu this weekend, book your table now.</span></div>
        <div class="post"><i></i><span>Thank you to everyone who joined our wine night.</span></div>
        <div class="post"><i></i><span>Fresh ravioli on the chalkboard tonight.</span></div>
        <div class="post"><i></i><span>Gift certificates are now available online.</span></div>
        <div class="post"><i></i><span>Live music every Friday from eight.</span></div>
        <div class="post"><i></i><span>Our sommelier picks the wine of the month.</span></div>
      </div>
    </div>
    <div class="fcol">
      <h5>Wandermeter</h5>
      <div class="widget review">
        <div class="title">Wandermeter</div>
        <b>Vinora Bistro</b>
        <span class="score">Rated 5.0 out of 5</span>
        <span>#3 of 420 restaurants in Cabo San Lucas</span>
        <hr>
        <b>Latest review</b>
        <span class="score">5.0 out of 5</span>
        <span>Wonderful food and a very friendly team. The wine pairing was the highlight of our trip. We will be back.</span>
        <hr>
        <span class="score">5.0 out of 5</span>
        <span>Cozy room, great pasta and the best tiramisu in town.</span>
      </div>
    </div>
    <div class="fcol">
      <h5>Locate Us</h5>
      <div class="map" role="img" aria-label="Street map showing the restaurant location near the marina"></div>
    </div>
  </div>
</footer>
<div class="bottom-bar">© Vinora Bistro. All rights reserved.</div>

</body>
</html>
```